Web Design Project

We need a web design for a new company that we started called ZARN CNG. ZARN CNG is a company that will build, own and operate compressed natural gas fueling stations throughout the United States. Our primary customers are Trucking companies and the stations will be built for semi trucks. CNG is better for the environment than diesel fuel, and will save trucking companies loads of money. It is also a domestic product which means that it will create American jobs and help America become energy independent. I have attached a logo that we are using. We dont need to stay with this logo persay, but it is what we have for now. We have a video on Vidlo that shows a bit of what we are doing. just search for ZARN CNG. ZARN CNG is a sister company of Holtmark of Arizona,www.hkqvz.example and a nationwide distributor of TRIVEX FUEL, www.trivexfuel.example. We will need links to these sites. Please make any pictures of trucks Holtmark trucks, and please do not use pictures of cabover trucks.

Target Market(s)

The target market are truck drivers and truckers.

Industry/Entity Type

Environment

Requirements
Must have
• Map showing station locations, a page with industry news, a page with a savings calculator (we can code the calculator) Site should have links to

```html
<!DOCTYPE html>
<html lang="en">
<head>
<meta charset="utf-8">
<title>ZARN CNG</title>
<link rel="stylesheet" href="https://fonts.googleapis.com/css2?family=Roboto+Condensed:wght@400;700&family=PT+Sans:wght@400;700&family=Arimo:wght@400;700&display=swap">
<style>
  :root {
    --green: #3aa635;
    --green-dark: #1f7a1f;
    --green-deep: #0f6a2a;
    --grey-text: #7d7d7d;
    --body-text: #222;
    --hero-grey: #8f8f8f;
    --red: #8c0a0a;
    --charcoal: #262626;
    --footer: #7a7a7a;
    --white: #fff;
  }
  * { margin: 0; padding: 0; box-sizing: border-box; }
  html, body { width: 1200px; height: 1116px; overflow: hidden; background: var(--white); }
  body { position: relative; font-family: "PT Sans", sans-serif; color: var(--body-text); }
  .abs { position: absolute; }

  .header-band { left: 0; top: 0; width: 1200px; height: 128px; background: linear-gradient(#ffffff, #e9e9e9); }
  .brand { left: 181px; top: 27px; font-family: "Roboto Condensed", sans-serif; font-weight: 700; font-size: 38px; color: var(--green); letter-spacing: 0; line-height: 40px; }
  .call { left: 907px; top: 32px; font-family: "Roboto Condensed", sans-serif; line-height: 19px; }
  .call .label { font-size: 17px; color: #555; }
  .call .phone { font-size: 17px; color: var(--green); }

  .nav { left: 180px; top: 90px; width: 840px; height: 37px; background: linear-gradient(#4cb845, #2d9a2a); border-bottom: 1px solid #237c22; }
  .nav a { position: absolute; top: 0; line-height: 37px; transform: translateX(-50%); color: var(--white); font-family: "Roboto Condensed", sans-serif; font-size: 13.5px; text-decoration: none; white-space: nowrap; }

  .hero { left: 180px; top: 128px; width: 840px; height: 304px; background: linear-gradient(#e8e8e8 0%, #b3b3b3 40%, var(--hero-grey) 100%); }
  .hero-art { left: 420px; top: 171px; width: 592px; height: 260px; background: radial-gradient(ellipse at 40% 55%, #3fae3a 0%, #5f8a5c 30%, #6d6d6d 60%, rgba(120,120,120,0) 80%); opacity: .85; }
  .hero-title { left: 217px; top: 202px; font-family: "Roboto Condensed", sans-serif; font-size: 27px; line-height: 28px; }
  .hero-title .g { color: var(--green); }
  .hero-title .k { color: #111; }
  .hero-sub { left: 221px; top: 265px; font-family: "Roboto Condensed", sans-serif; font-size: 15px; line-height: 22px; color: var(--white); }
  .hero-copy { left: 224px; top: 316px; width: 215px; font-family: "Arimo", sans-serif; font-size: 8.3px; line-height: 15.5px; color: var(--white); }
  .dots { left: 954px; top: 412px; display: flex; gap: 3px; }
  .dots span { width: 8px; height: 8px; background: #d6d6d6; }
  .dots span.on { background: var(--green); }

  .truckers { left: 180px; top: 433px; width: 840px; height: 168px; background: linear-gradient(#9c9c9c, #f4f4f4 85%, #fff); }
  .truck-art { left: 840px; top: 437px; width: 180px; height: 163px; background: linear-gradient(#c5c5c5, #9b2b35 55%, #e8e8e8); }
  .truckers h2 { position: absolute; left: 26px; top: 17px; font-family: "Roboto Condensed", sans-serif; font-weight: 400; font-size: 29px; line-height: 31px; color: var(--white); }
  .truckers h2 .g { color: var(--green-deep); }
  .truckers p { position: absolute; left: 28px; top: 93px; width: 640px; font-size: 9.2px; line-height: 15.5px; }
  .btn { display: block; background: linear-gradient(#5cc14f, #2e9526); border: 1px solid #257a1f; border-radius: 2px; color: var(--white); text-align: center; text-decoration: none; font-family: "PT Sans", sans-serif; }
  .btn-lg { width: 111px; height: 29px; line-height: 27px; font-size: 15px; }
  .divider { left: 180px; top: 602px; width: 840px; height: 1px; background: #dcdcdc; }

  .section-title { font-family: "Roboto Condensed", sans-serif; font-size: 29px; color: var(--grey-text); line-height: 30px; white-space: nowrap; }
  .section-title .g { color: var(--green-deep); }
  .section-title small { font-size: 22px; }
  .copy { font-size: 9.3px; line-height: 15.5px; text-align: justify; }
  .gears { left: 180px; top: 659px; width: 221px; height: 85px; border: 2px solid #ccc; background: linear-gradient(90deg, #5a5a5a, #b5b5b5 60%, #8a8a8a); }

  .promo { left: 180px; top: 830px; width: 398px; height: 192px; background: var(--red); }
  .promo-top { left: 180px; top: 830px; width: 398px; height: 68px; background: var(--charcoal); }
  .person { left: 403px; top: 819px; width: 171px; height: 203px; background: linear-gradient(#c7a58c, #8d8d8d 45%, #6e6e6e); border-radius: 60px 60px 0 0; }
  .promo-for { left: 197px; top: 842px; font-family: "Arimo", sans-serif; font-weight: 700; font-size: 15px; color: var(--green); }
  .promo-title { left: 197px; top: 858px; font-family: "Roboto Condensed", sans-serif; font-size: 31px; color: var(--white); line-height: 34px; }
  .promo-copy { left: 197px; top: 907px; width: 210px; font-family: "Arimo", sans-serif; font-size: 9px; line-height: 13.7px; color: var(--white); }
  .btn-sm { width: 70px; height: 18px; line-height: 16px; font-size: 10.5px; }

  .map { left: 611px; top: 830px; width: 408px; height: 192px; border: 4px solid #d3d3d3; background: radial-gradient(ellipse at 50% 45%, #d9dcb8 0%, #cfd6b0 45%, #a9c3dc 75%); }

  .footer { left: 0; top: 1052px; width: 1200px; height: 64px; background: var(--footer); }
  .footer-links { left: 189px; top: 1070px; display: flex; font-family: "Arimo", sans-serif; font-size: 7.8px; color: var(--white); }
  .footer-links a { color: var(--white); text-decoration: none; }
  .footer-links .sep { margin: 0 14px; }
  .copyright { left: 189px; top: 1089px; font-family: "Arimo", sans-serif; font-size: 7.8px; color: var(--white); }
  .social { left: 934px; top: 1073px; display: flex; gap: 7px; }
  .social span { width: 22px; height: 22px; border-radius: 3px; background: #4a8fc8; border: 1px solid #eee; }
</style>
</head>
<body>
  <div class="abs header-band"></div>
  <div class="abs brand">ZARN CNG</div>
  <div class="abs call"><div class="label">CALL US :</div><div class="phone">00 0000 000 000</div></div>

  <nav class="abs nav">
    <a href="#" style="left:54px">HOME</a>
    <a href="#" style="left:160px">FEATURE</a>
    <a href="#" style="left:289px">HOW IT WORKS</a>
    <a href="#" style="left:420px">ABOUT US</a>
    <a href="#" style="left:553px">MONEY SAVING</a>
    <a href="#" style="left:670px">MAP</a>
    <a href="#" style="left:781px">CONTACT US</a>
  </nav>

  <section class="abs hero"></section>
  <div class="abs hero-art" role="img" aria-label="Green arrows, green CNG gas cylinders and a black hatchback car"></div>
  <h1 class="abs hero-title" style="font-weight:400"><span class="g">THIS IS MORE</span><br><span class="k">ECONOMIC ON MONEY</span></h1>
  <div class="abs hero-sub">AND BETTER THAN DIESEL AND<br>MORE SAFE TO THE ECOLOGY</div>
  <p class="abs hero-copy">LOREM IPSUM IS SIMPLY DUMMY TEXT OF THE PRINTING AND TYPESETTING INDUSTRY. LOREM IPSUM HAS BEEN THE INDUSTRY'S.</p>
  <div class="abs dots"><span class="on"></span><span></span><span></span><span></span><span></span></div>

  <section class="abs truckers">
    <h2>Our customers are<br><span class="g">trucking companies and semi trucks.</span></h2>
    <p>Lorem Ipsum is simply dummy text of the printing and typesetting industry. Lorem Ipsum has been the industry's standard dummy text ever since the 1500s, when an unknown printer took a galley of type and scrambled it to make a type specimen book.</p>
  </section>
  <div class="abs truck-art" role="img" aria-label="Red semi truck with a silver trailer"></div>
  <a class="abs btn btn-lg" href="#" style="left:715px;top:555px">Readmore</a>
  <div class="abs divider"></div>

  <h2 class="abs section-title" style="left:181px;top:616px;font-weight:400">Welcome to <span class="g">ZARN <small>CNG</small></span></h2>
  <div class="abs gears" role="img" aria-label="Hand touching a cluster of gears in greyscale"></div>
  <p class="abs copy" style="left:415px;top:662px;width:262px">Lorem Ipsum is simply dummy text of the printing and typesetting industry. Lorem Ipsum has been the industry's standard dummy text ever since the 1500s, when an unknown printer took a galley of type and scrambled it to make a type specimen book. It has survived not only five centuries, but also the leap into electronic</p>
  <p class="abs copy" style="left:181px;top:756px;width:496px">Lorem Ipsum is simply dummy text of the printing and typesetting industry. Lorem Ipsum has been the industry's standard dummy text ever since the 1500s, when an unknown printer took a galley of type and scrambled it to make a type specimen book. It has survived not only five centuries, but also the leap into electronic</p>

  <h2 class="abs section-title" style="left:715px;top:619px;font-weight:400">About <span class="g">ZARN <small>CNG</small></span></h2>
  <p class="abs copy" style="left:715px;top:658px;width:304px">Lorem Ipsum is simply dummy text of the printing and typesetting industry. Lorem Ipsum has been the industry's standard dummy text ever since the 1500s, when an unknown printer took a galley of type and scrambled it to make a type specimen book.</p>
  <p class="abs copy" style="left:715px;top:735px;width:304px">galley of type and scrambled it to make a type specimen book. It has survived not only five centuries, but also the leap into electronic</p>
  <a class="abs btn btn-lg" href="#" style="left:916px;top:772px;width:101px">Readmore</a>

  <div class="abs promo"></div>
  <div class="abs promo-top"></div>
  <div class="abs person" role="img" aria-label="Smiling businessman in a grey suit gesturing with an open hand"></div>
  <div class="abs promo-for">FOR</div>
  <div class="abs promo-title">MONEY SAVING</div>
  <div class="abs promo-copy">
    <p>Lorem Ipsum is simply dummy text of the printing and typesetting industry. Lorem Ipsum has been the industry's standard.</p>
    <p style="margin-top:13.7px">Lorem Ipsum is simply dummy text of the printing and typesetting industry.</p>
  </div>
  <a class="abs btn btn-sm" href="#" style="left:323px;top:994px">Read more</a>

  <div class="abs map" role="img" aria-label="Map of the United States showing station locations"></div>

  <footer class="abs footer"></footer>
  <div class="abs footer-links">
    <a href="#">HOME</a><span class="sep">|</span>
    <a href="#">FEATURE</a><span class="sep">|</span>
    <a href="#">HOW IT WORKS</a><span class="sep">|</span>
    <a href="#">ABOUT US</a><span class="sep">|</span>
    <a href="#">SERVICES</a><span class="sep">|</span>
    <a href="#">CONTACT US</a>
  </div>
  <div class="abs copyright">COPYRIGHT © 2012. ZARN CNG. ALL RIGHTS RESERVED.</div>
  <div class="abs social"><span></span><span></span><span></span></div>
</body>
</html>
```